Greeting card special spring

Context: I missed the end of the year wishes and would like to send my clients a spring card with a smell of lily of the valley that is 11cm by 11 cm and has a vintage look. This A5 card will be sent in a green envelope with the small ordering bag. I will like the target notes the intent and the associated gaiety My business is HR / Leadership and my clients are responsible for business or HR. Esprit: To keep a spirit of sobriete and elegance but with gaiety. Color: our graphic charter is generally black and gray but for this theme we can shift in color more "spring" taking again the green of the sachet of lily of the valley which is joined in particular to illustrate the notions energy, renewal. (Attached the picture). No photo. Just text and logo. Play on composition and fonts; I have put the elements of typos and fonts as well as taglines and examples of compositions already made (business card, correspondence card, letter paper). One of the elements of the graphic chart is an "e" that is done in brush. If you wish you can play with this graphic elements. Also look at the picture of the perfume pouch that I would attach Format: a card a format A5 or format postcard (format printolux). The text is composed of 2 elements: Major Text The Quorvana team wishes you a spring full of renewal, fulfillment and creative energy to disseminate absolutely around you. Text minor: Lily of the Valley: Omen of happiness that brings luck to breathe with serenity! Include Logo See contact details Marthe Lubois-Cagnat - marthe.lubois@quorvana-mail.com

Target Market(s)

Senior managers, human resource managers

Industry/Entity Type

Management Consulting

Other font styles liked:
• merci d'essayer de rester aligner ou en logique avec les polices/charte graphique envoyees

Requirements
Must have
• Format: one card in A5 format or postcard format (printolux format). The text is composed of 2 elements: Major Text The Quorvana team wishes you a spring full of renewal, fulfillment and creative energy to disseminate absolutely around you. Text minor: Lily of the Valley: Omen of happiness that brings luck to breathe with serenity! Include Logo See contact details Marthe Lubois-Cagnat - marthe.lubois@quorvana-mail.com
Nice to have
• Graphical guideline :. Esprit: To keep a spirit of sobriete and elegance but with gaiety. Color: our graphic charter is generally black and gray but for this theme we can shift in color more "spring" taking again the green of the sachet of lily of the valley which is joined in particular to illustrate the notions energy, renewal. (Attached the picture). Grapic elements; I have put the elements of typos and fonts as well as the examples of compositions already made (business card, correspondence card, letter paper). One of the elements of the logo is an "e" that is made in brush on which you can play. Also look at the image of the perfume pouch that I would join
Should not have
• No photo. Just text and logo. Play on composition and fonts

```html
<!DOCTYPE html>
<html lang="fr">
<head>
<meta charset="utf-8">
<title>Carte de printemps – Quorvana</title>
<link rel="stylesheet" href="https://fonts.googleapis.com/css2?family=Playfair+Display:ital,wght@1,400&family=Allura&family=Montserrat:wght@400&display=swap">
<style>
  :root {
    --paper: #ffffff;
    --frame-green: #3b8a2e;
    --script-green: #3f7a2a;
    --text-grey: #767676;
    --ink: #1c1c1c;
    --contact-grey: #6a6a6a;
    --leaf-dark: #2f6b2a;
    --leaf-light: #a9c98f;
  }
  html, body {
    margin: 0;
    padding: 0;
    overflow: hidden;
    background: var(--paper);
  }
  .card {
    position: relative;
    width: 847px;
    height: 1200px;
    background: var(--paper);
    overflow: hidden;
  }
  .card-frame {
    position: absolute;
    inset: 0;
  }
  .headline {
    position: absolute;
    top: 188px;
    left: 0;
    width: 847px;
    margin: 0;
    text-align: center;
    font-family: "Playfair Display", serif;
    font-style: italic;
    font-weight: 400;
    font-size: 58px;
    color: var(--text-grey);
  }
  .wish {
    position: absolute;
    top: 312px;
    left: 112px;
    width: 620px;
    margin: 0;
    text-align: center;
    font-family: "Playfair Display", serif;
    font-style: italic;
    font-size: 47px;
    line-height: 62px;
    color: var(--text-grey);
  }
  .lily-illustration {
    position: absolute;
    left: 140px;
    top: 735px;
    width: 122px;
    height: 192px;
    border-radius: 60% 40% 20% 50%;
    background: linear-gradient(160deg, var(--leaf-light) 0%, #eef3ea 40%, var(--leaf-dark) 100%);
  }
  .lily-note {
    position: absolute;
    top: 780px;
    left: 255px;
    width: 460px;
    margin: 0;
    text-align: center;
    font-family: "Allura", cursive;
    font-size: 38px;
    line-height: 54px;
    color: var(--script-green);
  }
  .brand {
    position: absolute;
    top: 1010px;
    left: 0;
    width: 847px;
    text-align: center;
  }
  .brand-dot {
    display: block;
    width: 40px;
    height: 40px;
    margin: 0 auto 18px;
    border-radius: 50%;
    background: var(--ink);
  }
  .brand-name {
    display: block;
    font-family: "Montserrat", sans-serif;
    font-size: 16px;
    letter-spacing: 6px;
    padding-left: 6px;
    color: var(--ink);
  }
  .contact {
    position: absolute;
    top: 1104px;
    left: 0;
    width: 847px;
    margin: 0;
    text-align: center;
    font-family: "Montserrat", sans-serif;
    font-size: 16px;
    line-height: 22px;
    color: var(--contact-grey);
  }
</style>
</head>
<body>
<main class="card">
  <svg class="card-frame" width="847" height="1200" viewBox="0 0 847 1200" aria-hidden="true">
    <g fill="none" stroke="var(--frame-green)" stroke-width="3">
      <line x1="36" y1="24" x2="811" y2="24"/>
      <line x1="36" y1="1173" x2="811" y2="1173"/>
      <line x1="36" y1="24" x2="36" y2="1173"/>
      <line x1="811" y1="24" x2="811" y2="1173"/>
      <rect x="36" y="40" width="20" height="20"/>
      <rect x="791" y="40" width="20" height="20"/>
      <rect x="36" y="1137" width="20" height="20"/>
      <rect x="791" y="1137" width="20" height="20"/>
    </g>
  </svg>

  <h1 class="headline">L’équipe de Quorvana</h1>

  <p class="wish">vous souhaite un printemps plein de renou-veau, d’épanouissement et d’éngie créatrice à diffuser absolument autour de vous.</p>

  <div class="lily-illustration" role="img" aria-label="Brin de muguet avec sa feuille verte"></div>

  <p class="lily-note">Muguet: présage de bonheur<br>qui porte chance à respirer avec<br>sérénité !</p>

  <div class="brand">
    <span class="brand-dot"></span>
    <span class="brand-name">QUORVANA</span>
  </div>

  <p class="contact">Marthe Lubois-Cagnat<br>marthe.lubois@quorvana-mail.com</p>
</main>
</body>
</html>
```